BRSP Business Card Design Project

We are a Wedding Film company in Charleston, SC In need of a unique business card. Our website is www.brightspiralreels.example. Check us out to get an idea of who we are and what we do. The design should be upscale but not pretentious. Modern but not cheesy. I will most likely have our cards printed by Zib on the Opal design. I'm also liking the raised designs for our logo. The Wedding Films in our logo on our site is blue so feel free to manipulate our logo for your designs as well.

Industry/Entity Type

Business

Requirements
Must have
• This is the info I want on the card:

Derek Hollisbury
Storyteller

Brightspiral Wedding Reels
www.brightspiralreels.example

555.208.4417
derek@brightspiralreels.example

```html
<!DOCTYPE html>
<html lang="en">
<head>
<meta charset="utf-8">
<title>Brightspiral Wedding Reels – Business Card</title>
<link href="https://fonts.googleapis.com/css2?family=Questrial&family=Petit+Formal+Script&display=swap" rel="stylesheet">
<style>
  :root {
    --stage: #4a4a4c;
    --gold-deep: #8e7545;
    --gold-mid: #a48b58;
    --gold-light: #c8bb7c;
    --pearl: #eef2f3;
    --pearl-shade: #d3dcdf;
    --ink: #1f1f1f;
    --white: #ffffff;
  }
  * { margin: 0; padding: 0; box-sizing: border-box; }
  html, body { width: 1200px; height: 534px; overflow: hidden; }
  body {
    background: var(--stage);
    position: relative;
    font-family: "Questrial", sans-serif;
  }
  .card {
    position: absolute;
    top: 119px;
    width: 517px;
    height: 293px;
    border-radius: 20px;
    overflow: hidden;
  }
  .card--front {
    left: 62px;
    background: linear-gradient(90deg, var(--gold-deep) 0%, var(--gold-mid) 30%, var(--gold-light) 58%, var(--gold-mid) 80%, var(--gold-deep) 100%);
  }
  .card--back {
    left: 620px;
    background: radial-gradient(ellipse at 50% 30%, var(--white) 0%, var(--pearl) 45%, var(--pearl-shade) 100%);
  }
  .brand-name {
    position: absolute;
    font-family: "Questrial", sans-serif;
    font-weight: 400;
    text-align: center;
    line-height: 1.1;
  }
  .card--front .brand-name {
    left: 0; right: 0;
    top: 118px;
    font-size: 36px;
    color: var(--white);
  }
  .card--back .brand-name {
    left: 22px;
    width: 200px;
    top: 78px;
    font-size: 24px;
    color: var(--gold-mid);
  }
  .person {
    position: absolute;
    left: 232px;
    top: 84px;
    display: flex;
    align-items: baseline;
    gap: 8px;
  }
  .person__name {
    font-family: "Petit Formal Script", cursive;
    font-size: 20px;
    color: var(--gold-deep);
  }
  .person__role {
    font-size: 12px;
    color: var(--ink);
  }
  .name-rule {
    position: absolute;
    left: 232px;
    right: 0;
    top: 113px;
    height: 5px;
    background: var(--gold-deep);
  }
  .contact {
    position: absolute;
    left: 232px;
    top: 128px;
    list-style: none;
  }
  .contact li {
    font-size: 12.5px;
    color: var(--ink);
    line-height: 18px;
    white-space: nowrap;
  }
  .contact__label {
    font-family: "Petit Formal Script", cursive;
    font-size: 10px;
    color: var(--gold-deep);
    margin-right: 4px;
  }
  .band {
    position: absolute;
    left: 0; right: 0;
    top: 211px;
    height: 48px;
    background: linear-gradient(90deg, var(--gold-deep) 0%, var(--gold-mid) 35%, var(--gold-light) 55%, var(--gold-mid) 75%, var(--gold-deep) 100%);
  }
</style>
</head>
<body>
  <section class="card card--front" aria-label="Card front">
    <p class="brand-name">Brightspiral Wedding Reels</p>
  </section>

  <section class="card card--back" aria-label="Card back">
    <p class="brand-name">Brightspiral Wedding Reels</p>
    <div class="person">
      <span class="person__name">Derek Hollisbury</span>
      <span class="person__role">Storyteller</span>
    </div>
    <div class="name-rule"></div>
    <ul class="contact">
      <li><span class="contact__label">phone :</span>+ 555.208.4417</li>
      <li><span class="contact__label">email :</span>derek@brightspiralreels.example</li>
      <li><span class="contact__label">website :</span>www.brightspiralreels.example</li>
    </ul>
    <div class="band"></div>
  </section>
</body>
</html>
```